Community Legal Website

The website is about a law in legal area (Fiscal), it has a moderator and the community also contributes with information.

Attention that this is not for a Law Firm. This is a community site where all the lawyers can contribute wiith their knowledge and at the same time where they can read the Official Law in the fiscal area.

The site is in portuguese, but we have attach information in english about the functionalities.

I attach information which represents the first version of the site done by html.. That is the site we intend to improve.

The site is quite simple because the main pages are:
- Home page;
- Section page (which has the Chapters and articles)
- Article page;

This pages all belong to the article:

redaccao_actual.htm, redaccoes_anteriores.htm, anotacoes.htm, jurisprudencia.htm, decisoesadministrativas.htm, minutas.htm, duvidas.htm

AS you see in all of them the options are always there.

The most important in this site is the usability of the content:

The FAQ, Contacts, Terms of conditions, who we are, are links less important.

Also there is a possibility to have in the homepage a higligh of certain articles that we want to raise from the others.

Please check the excel sheet as well as the zip file wich has the site in portuguese that you can use a website translator to check in your language.
Updates

We added a excel sheet with the functionalities in english which the site must have.

Reason: Because this is easter time we have increased the time for the deliver

Please check briefing update.

Reason: There were some request to extend the deadline because of the Easter

Hi!

Please read carefully the briefing. People are presenting me company web sites adn this is NOT a company web site. THis is a Site wich has a content of Laws. Please check the 1st version in the zip file and improve it. The options are there and you can translate in google tradutor or reading the excel sheet attach.

txs,
JV

Reason: My client need more desing choices

Target Market(s)

Lawyers, jurists and people related with the fiscal Law.

Industry/Entity Type

Legal

Requirements
Must have
• The interface should be clean and elegant.
It should also contribute to speed.
And try to avoid to many distract elements.
The site will be dinamic and with a backoffice, so in that you have to be carefully with the space dynamic. But you don't have to worry about the backoffice. Only the front office which is the public site.

```html
<!DOCTYPE html>
<html lang="pt">
<head>
<meta charset="utf-8">
<title>Código do IRS – Artigo 32</title>
<link href="https://fonts.googleapis.com/css2?family=Cabin:wght@500;600;700&family=Open+Sans:wght@400;600&family=Signika:wght@300;400&display=swap" rel="stylesheet">
<style>
:root{
  --slate:#526a63;
  --slate-dark:#44574f;
  --charcoal:#4a4a4a;
  --ink:#3e5751;
  --text:#8b8b8b;
  --text-dark:#2f2f2f;
  --rule:#d2d2d2;
  --white:#ffffff;
  --star-off:#b9b9b9;
}
*{box-sizing:border-box;margin:0;padding:0}
html,body{width:960px;height:1200px;overflow:hidden;background:var(--white)}
body{position:relative;font-family:"Signika",sans-serif;color:var(--text)}
a{color:inherit;text-decoration:none}
.abs{position:absolute}

/* header */
.header{position:absolute;left:0;top:0;width:960px;height:76px;background:var(--charcoal)}
.header .strip{position:absolute;left:0;top:0;width:960px;height:23px;background:var(--slate)}
.brand{position:absolute;left:151px;top:0;width:266px;height:65px;background:linear-gradient(#fff,#e9e9e9);border-radius:0 0 4px 4px;box-shadow:0 1px 3px rgba(0,0,0,.4);display:flex;align-items:center;gap:10px;padding-left:14px}
.brand .mark{width:32px;height:32px;background:var(--slate)}
.brand .name{font-family:"Cabin",sans-serif;font-weight:700;font-size:18px;color:var(--slate-dark);letter-spacing:.2px}
.util-links{position:absolute;top:5px;left:468px;display:flex;gap:19px;font-size:10.5px;color:var(--white);font-weight:300}
.tool-links{position:absolute;top:46px;left:512px;display:flex;font-size:10px;color:#cfcfcf;font-weight:300}
.tool-links a{padding:0 10px;border-left:1px solid #5e5e5e;line-height:22px}
.tool-links a:first-child{border-left:0}

/* tabs */
.tabs{position:absolute;left:144px;top:76px;width:672px;height:42px;display:flex;align-items:center;font-size:10px;color:var(--text-dark);font-weight:300}
.tabs a{padding:0 9.5px;height:42px;line-height:52px}
.tabs a:first-child{padding-left:9px}
.tabs a.active{background:var(--charcoal);color:var(--white)}
.btn-comment{position:absolute;left:730px;top:87px;width:80px;height:25px;background:var(--slate);color:var(--white);border-radius:3px;font-size:10px;text-align:center;line-height:25px;font-weight:300}
.tabs-rule{position:absolute;left:0;top:117px;width:960px;height:2px;border-top:1px solid var(--rule);border-bottom:1px solid #eee}

/* bands */
.band{position:absolute;left:144px;width:672px;height:43px;background:var(--slate);color:var(--white);font-family:"Cabin",sans-serif}
.band.title{top:126px;text-align:center;font-weight:600;font-size:13px;line-height:43px}
.band.more{top:594px;font-weight:500;font-size:15px;line-height:43px;padding-left:9px}

/* entries */
.meta{position:absolute;left:144px;width:672px;height:14px;font-size:9.5px;color:var(--slate-dark);font-weight:300}
.meta span,.meta svg{position:absolute;top:0}
.meta .i-user{left:10px;top:1px}
.meta .author{left:34px}
.meta .i-clock{left:114px;top:1px}
.meta .date{left:142px}
.meta .i-talk{left:212px;top:1px}
.meta .count{left:229px}
.meta .rate-label{left:546px}
.meta .stars{left:602px;top:0;display:flex;gap:1.5px}
.entry-title{position:absolute;left:155px;font-family:"Cabin",sans-serif;font-weight:600;font-size:13.5px;color:var(--ink);line-height:18px;width:560px}
.lede{position:absolute;left:154px;font-family:"Open Sans",sans-serif;font-size:8px;color:var(--text-dark)}
.excerpt{position:absolute;left:154px;width:640px;font-family:"Open Sans",sans-serif;font-size:7.9px;line-height:12px;color:var(--text)}
.excerpt a{color:var(--ink);text-decoration:underline;font-weight:600}
.btn-more{position:absolute;left:154px;width:57px;height:24px;border-radius:3px;background:var(--slate);color:var(--white);font-size:9.5px;text-align:center;line-height:24px;font-weight:300}
.btn-share{position:absolute;left:154px;width:57px;height:24px;border-radius:3px;background:var(--charcoal);color:var(--white);font-size:9.5px;text-align:center;line-height:24px;font-weight:300}
.share-dots{position:absolute;left:227px;display:flex;gap:8px}
.share-dots i{display:block;width:16px;height:16px;background:#7a7a7a;border-radius:2px}
.rule{position:absolute;left:143px;width:673px;height:1px;background:var(--rule)}

/* pager */
.pager{position:absolute;left:146px;top:1076px;height:20px;display:flex;align-items:center;font-size:10px;color:var(--slate-dark)}
.pager .prev,.pager .next{height:20px;line-height:20px;background:var(--slate);color:var(--white);font-weight:300;padding:0 9px;border-radius:2px}
.pager .prev{clip-path:polygon(7px 0,100% 0,100% 100%,7px 100%,0 50%);padding-left:12px}
.pager .next{clip-path:polygon(0 0,calc(100% - 7px) 0,100% 50%,calc(100% - 7px) 100%,0 100%);padding-right:12px}
.pager .pages{display:flex;gap:12px;margin:0 19px 0 14px}
.pager .pages b{color:var(--text-dark)}

/* footer */
.footer{position:absolute;left:0;top:1152px;width:960px;height:48px;background:var(--charcoal);font-size:9.5px;color:#c4c4c4;font-weight:300}
.footer nav{position:absolute;left:148px;top:13px;display:flex}
.footer nav a{padding:0 8px;border-left:1px solid #5e5e5e;line-height:22px}
.footer nav a:first-child{border-left:0}
.footer .copy{position:absolute;left:596px;top:19px}
</style>
</head>
<body>

<svg width="0" height="0" style="position:absolute">
  <defs>
    <symbol id="star" viewBox="0 0 20 20"><polygon points="10,1 12.6,7 19,7.4 14,11.6 15.6,18 10,14.5 4.4,18 6,11.6 1,7.4 7.4,7"/></symbol>
    <symbol id="user" viewBox="0 0 12 12"><circle cx="6" cy="3.5" r="3"/><path d="M0 12c0-3.5 2.5-5 6-5s6 1.5 6 5z"/></symbol>
    <symbol id="clock" viewBox="0 0 12 12"><circle cx="6" cy="6" r="5" fill="none" stroke="currentColor" stroke-width="1.4"/><path d="M6 3v3.4h2.6" fill="none" stroke="currentColor" stroke-width="1.3"/></symbol>
    <symbol id="talk" viewBox="0 0 12 12"><path d="M1 1h7v5H4L2 8V6H1z"/><path d="M9 4h2v5h-1v2l-2-2H5V7h4z"/></symbol>
  </defs>
</svg>

<header class="header">
  <div class="strip"></div>
  <a class="brand" href="#"><span class="mark"></span><span class="name">SERRA VALENTE.net</span></a>
  <nav class="util-links"><a href="#">Termos de utilização</a><a href="#">Perguntas frequentes</a><a href="#">Quem somos</a><a href="#">CONTACTOS</a></nav>
  <nav class="tool-links"><a href="#">Índice deste Código</a><a href="#">Menu dos Códigos</a><a href="#">Gravar</a><a href="#">Imprimir</a></nav>
</header>

<nav class="tabs">
  <a href="#">Redacção actual</a><a href="#">Redacções anteriores</a><a class="active" href="#">Anotações</a><a href="#">Jurisprudência</a><a href="#">Decisões administrativas</a><a href="#">Minutas</a><a href="#">Dúvidas</a>
</nav>
<a class="btn-comment" href="#">Comentar</a>
<div class="tabs-rule"></div>

<h1 class="band title">CÓDIGO DO IRS - Artigo 32 : Encargos não dedutíveis para efeitos fiscais</h1>

<!-- annotation 1 -->
<div class="meta" style="top:192px">
  <svg class="i-user" width="11" height="11" fill="currentColor"><use href="#user"/></svg><span class="author">Serra Valente</span>
  <svg class="i-clock" width="11" height="11" fill="currentColor" style="color:var(--slate-dark)"><use href="#clock"/></svg><span class="date">22.10.2012</span>
  <svg class="i-talk" width="11" height="11" fill="currentColor"><use href="#talk"/></svg><span class="count">10 Comentar</span>
  <span class="rate-label">Classificar</span>
  <span class="stars"><svg width="11" height="11" fill="var(--slate)"><use href="#star"/></svg><svg width="11" height="11" fill="var(--slate)"><use href="#star"/></svg><svg width="11" height="11" fill="var(--slate)"><use href="#star"/></svg><svg width="11" height="11" fill="var(--slate)"><use href="#star"/></svg><svg width="11" height="11" fill="var(--slate)"><use href="#star"/></svg></span>
</div>
<h2 class="entry-title" style="top:217px;left:154px">Como distinguir os encargos dedutíveis dos encargos parafiscais</h2>
<p class="lede" style="top:241px">O penhor constitui um direito real de garantia que confere uma preferência ao credor pignoratício sobre coisas ou direitos não hipotecáveis.</p>
<p class="excerpt" style="top:265px">Esta figura jurídica encontra-se definida no n.º 1 do art.º 666.º do Código Civil, o qual dispõe que: “O penhor confere ao credor o direito à satisfação do seu crédito, bem como dos juros, se os houver, com preferência sobre os demais credores, pelo valor de certa coisa móvel, ou pelo valor de créditos ou outros direitos não susceptíveisalor de créditos ou outros direitos não susceptíveis de hipoteca, pertencentes ao devedor ou a ...</p>
<a class="btn-more" href="#" style="top:314px">Leia Mais</a>
<div class="rule" style="top:357px"></div>

<!-- annotation 2 -->
<div class="meta" style="top:380px">
  <svg class="i-user" width="11" height="11" fill="currentColor"><use href="#user"/></svg><span class="author">Luís Barreto</span>
  <svg class="i-clock" width="11" height="11" style="color:var(--slate-dark)"><use href="#clock"/></svg><span class="date">18.10.2012</span>
  <svg class="i-talk" width="11" height="11" fill="currentColor"><use href="#talk"/></svg><span class="count">10 Comentar</span>
  <span class="rate-label">Classificar</span>
  <span class="stars"><svg width="11" height="11" fill="var(--slate)"><use href="#star"/></svg><svg width="11" height="11" fill="var(--slate)"><use href="#star"/></svg><svg width="11" height="11" fill="var(--slate)"><use href="#star"/></svg><svg width="11" height="11" fill="var(--slate)"><use href="#star"/></svg><svg width="11" height="11" fill="var(--star-off)"><use href="#star"/></svg></span>
</div>
<h2 class="entry-title" style="top:404px">Despesas fiscais com investimento: provisões, suprimentos, despesas com a própria empresa e remunerações variáveis</h2>
<p class="excerpt" style="top:452px">"E isto porque é a Constituição que define e distribui as competências tributárias e que fixa os limites ao exercício do poder de tributar,limites que corúigum como verdadeiras garantias constitucionais do contribuinte, garante do justo equilíbrio entre o interesse do particular em.preservara sua esfera patrimonial. manifestação da sua liberdade, e o interesse do Fisco em assegurar para o Estado a cobertura das despesas públicas.</p>
<p class="excerpt" style="top:499px">Daí que, entre nós. se fale de uma "Constituição Fiscal", onde a legalidade tributária se configura como princípio fundamental que além de ser elemento essencial da distinção entre Finanças Públicas e Finanças Privadas. tem a dignidade constitucional de pressuposto r em.preservara sua esfera patrimonial. manifestação da sua liberdade, r em.preservara sua esfera patrimonial. patrimonial. patrimonial. ibutação, afirmando-se como a ...</p>
<a class="btn-more" href="#" style="top:550px">Leia Mais</a>

<h2 class="band more">Mais Artigos</h2>

<!-- more 1 -->
<div class="meta" style="top:653px">
  <svg class="i-user" width="11" height="11" fill="currentColor"><use href="#user"/></svg><span class="author">Anónimo</span>
  <svg class="i-clock" width="11" height="11" style="color:var(--slate-dark)"><use href="#clock"/></svg><span class="date">28.09.2012</span>
  <svg class="i-talk" width="11" height="11" fill="currentColor"><use href="#talk"/></svg><span class="count">10 Comentar</span>
  <span class="rate-label">Classificar</span>
  <span class="stars"><svg width="11" height="11" fill="var(--slate)"><use href="#star"/></svg><svg width="11" height="11" fill="var(--slate)"><use href="#star"/></svg><svg width="11" height="11" fill="var(--slate)"><use href="#star"/></svg><svg width="11" height="11" fill="var(--star-off)"><use href="#star"/></svg><svg width="11" height="11" fill="var(--star-off)"><use href="#star"/></svg></span>
</div>
<h3 class="entry-title" style="top:682px">Princípios de Direito Fiscal</h3>
<p class="excerpt" style="top:706px">Artigo publicado na Revista da ORCF, denso mas acessível. Para aceder a esta página da Internet, clique AQUI....</p>
<a class="btn-share" href="#" style="top:734px">Partilhar</a>
<div class="share-dots" style="top:740px"><i></i><i></i><i></i></div>
<div class="rule" style="top:772px"></div>

<!-- more 2 -->
<div class="meta" style="top:786px">
  <svg class="i-user" width="11" height="11" fill="currentColor"><use href="#user"/></svg><span class="author">Anónimo</span>
  <svg class="i-clock" width="11" height="11" style="color:var(--slate-dark)"><use href="#clock"/></svg><span class="date">21.09.2012</span>
  <svg class="i-talk" width="11" height="11" fill="currentColor"><use href="#talk"/></svg><span class="count">10 Comentar</span>
  <span class="rate-label">Classificar</span>
  <span class="stars"><svg width="11" height="11" fill="var(--slate)"><use href="#star"/></svg><svg width="11" height="11" fill="var(--slate)"><use href="#star"/></svg><svg width="11" height="11" fill="var(--slate)"><use href="#star"/></svg><svg width="11" height="11" fill="var(--star-off)"><use href="#star"/></svg><svg width="11" height="11" fill="var(--star-off)"><use href="#star"/></svg></span>
</div>
<h3 class="entry-title" style="top:816px">A Avaliação Geral dos Prédios Urbanos</h3>
<p class="excerpt" style="top:840px">Para aceder a esta página da Internet, clique <a href="#">AQUI</a>.</p>
<a class="btn-share" href="#" style="top:868px">Partilhar</a>
<div class="share-dots" style="top:874px"><i></i><i></i><i></i></div>
<div class="rule" style="top:907px"></div>

<!-- more 3 -->
<div class="meta" style="top:922px">
  <svg class="i-user" width="11" height="11" fill="currentColor"><use href="#user"/></svg><span class="author">Inês Valente</span>
  <svg class="i-clock" width="11" height="11" style="color:var(--slate-dark)"><use href="#clock"/></svg><span class="date">16.09.2012</span>
  <svg class="i-talk" width="11" height="11" fill="currentColor"><use href="#talk"/></svg><span class="count">10 Comentar</span>
  <span class="rate-label">Classificar</span>
  <span class="stars"><svg width="11" height="11" fill="var(--slate)"><use href="#star"/></svg><svg width="11" height="11" fill="var(--slate)"><use href="#star"/></svg><svg width="11" height="11" fill="var(--slate)"><use href="#star"/></svg><svg width="11" height="11" fill="var(--star-off)"><use href="#star"/></svg><svg width="11" height="11" fill="var(--star-off)"><use href="#star"/></svg></span>
</div>
<h3 class="entry-title" style="top:952px">Moura Campos - A Ditadura das Finanças</h3>
<p class="excerpt" style="top:976px">Para aceder a esta página da Internet, clique <a href="#">AQUI</a>.</p>
<a class="btn-share" href="#" style="top:1005px">Partilhar</a>
<div class="share-dots" style="top:1011px"><i></i><i></i><i></i></div>
<div class="rule" style="top:1050px"></div>

<nav class="pager">
  <a class="prev" href="#">anterior</a>
  <span class="pages"><b>1</b><a href="#">2</a><a href="#">3</a><a href="#">4</a><a href="#">5</a></span>
  <a class="next" href="#">próximo</a>
</nav>

<footer class="footer">
  <nav><a href="#">Índice deste Código</a><a href="#">Menu dos Códigos</a><a href="#">Gravar</a><a href="#">Imprimir</a></nav>
  <span class="copy">Copyright © 2013 SERRA VALENTE All Right Reserved</span>
</footer>

</body>
</html>
```